Power Generation Company needs a stationary design

We need a design for our letter envelope, A4 Envelope and letterhead. Our company name is BRIMVolt which i attached here sample our our call card. We are based in the Philippines and is into the Power Generation business. We own power facilities like Hydropower plant, Solar Power Plant, Diesel Power Plant, Gas Turbine Power Plant. We sell our power to various electric distribution companies, factories and office buildings.

Target Market(s)

Electric Distribution Companies and Factories

Industry/Entity Type

It Company

Colors
ec1f27

Requirements
Must have
• Logo and company name
Nice to have
• No specific
Should not have
• No specific

```html
<!DOCTYPE html>
<html lang="en">
<head>
<meta charset="utf-8">
<title>BRIMVolt Stationery</title>
<link rel="stylesheet" href="https://fonts.googleapis.com/css2?family=Lato:wght@300;400;700&family=Arimo:wght@400&family=Damion&display=swap">
<style>
  :root {
    --brand-red: #ec1f27;
    --paper: #ffffff;
    --ink: #1a1a1a;
    --backdrop: #d9dadc;
    --rule: #111111;
    --soft-grey: #e8e8e8;
  }
  * { margin: 0; padding: 0; box-sizing: border-box; }
  html, body { width: 1200px; height: 900px; overflow: hidden; }
  body { background: var(--backdrop); font-family: "Lato", sans-serif; color: var(--ink); position: relative; }

  .sheet { position: absolute; background: var(--paper); overflow: hidden; }
  .wordmark { position: absolute; color: var(--brand-red); font-family: "Lato", sans-serif; font-weight: 300; letter-spacing: 0.12em; white-space: nowrap; display: flex; align-items: center; gap: 0.3em; line-height: 1; }
  .wordmark .mark-dot { width: 0.8em; height: 0.8em; border: 1px solid currentColor; border-radius: 50%; }
  .wordmark.on-red { color: var(--paper); }

  .company-name { position: absolute; color: var(--brand-red); font-weight: 400; white-space: nowrap; }
  .contact-line { position: absolute; display: flex; align-items: center; gap: 3px; white-space: nowrap; color: var(--ink); }
  .contact-line svg { flex: none; }

  .address-band { position: absolute; left: 0; right: 0; background: var(--brand-red); color: var(--paper); text-align: center; white-space: nowrap; display: flex; align-items: center; justify-content: center; }
  .band-rule { position: absolute; left: 0; right: 0; background: var(--rule); }

  /* Letterhead */
  .letterhead { left: 33px; top: 30px; width: 454px; height: 587px; }
  .letterhead .wordmark { left: 35px; top: 40px; font-size: 20px; }
  .letterhead .company-name { left: 334px; top: 35px; font-size: 9px; }
  .letterhead .contact-line { left: 334px; font-size: 7.5px; }
  .recipient { position: absolute; left: 35px; top: 172px; font-family: "Arimo", sans-serif; }
  .recipient-name { font-size: 9px; letter-spacing: 0.02em; }
  .recipient-address { font-size: 7.4px; line-height: 9.5px; margin-top: 4px; }
  .letter-body { position: absolute; left: 35px; top: 232px; width: 381px; font-family: "Arimo", sans-serif; font-size: 7.9px; line-height: 13.4px; text-align: justify; }
  .letter-body p + p { margin-top: 13.4px; }
  .closing { position: absolute; left: 35px; top: 403px; font-family: "Arimo", sans-serif; font-size: 7.9px; }
  .signature { position: absolute; left: 35px; top: 430px; font-family: "Damion", cursive; font-size: 30px; line-height: 1; }
  .signatory { position: absolute; left: 35px; top: 470px; font-family: "Arimo", sans-serif; font-size: 8.5px; }
  .letterhead .address-band { top: 559px; height: 16px; font-size: 7.3px; }
  .letterhead .band-rule { top: 575px; height: 2px; }

  /* Envelopes */
  .envelope-flap { position: absolute; left: 0; top: 0; }
  .envelope-small { left: 508px; top: 31px; width: 316px; height: 382px; }
  .envelope-small .wordmark { left: 0; right: 0; top: 21px; justify-content: center; font-size: 13px; }
  .envelope-large { left: 702px; top: 634px; width: 457px; height: 229px; }
  .envelope-large .wordmark { left: 0; right: 0; top: 24px; justify-content: center; font-size: 16px; }

  /* Second-sheet letterhead */
  .continuation { left: 843px; top: 30px; width: 315px; height: 383px; }
  .continuation .wordmark { left: 20px; top: 24px; font-size: 13px; }
  .continuation .company-name { left: 20px; top: 331px; font-size: 5.5px; }
  .continuation .contact-line { left: 20px; font-size: 4.8px; }
  .continuation .address-band { top: 364px; height: 10px; font-size: 4.6px; }
  .continuation .band-rule { top: 374px; height: 1.5px; }

  /* Business cards */
  .card-front { left: 550px; top: 449px; width: 234px; height: 133px; background: var(--brand-red); border-radius: 4px; }
  .card-front .wordmark { left: 0; right: 0; top: 56px; justify-content: center; font-size: 19px; }
  .card-back { left: 883px; top: 448px; width: 235px; height: 134px; border-radius: 4px; }
  .card-back .wordmark { right: 12px; top: 17px; font-size: 15px; }
  .card-back .company-name { left: 13px; top: 48px; font-size: 9px; }
  .card-holder { position: absolute; left: 13px; top: 62px; font-size: 8px; font-weight: 700; }
  .card-address { position: absolute; left: 13px; top: 77px; font-size: 5.6px; line-height: 8.2px; }
  .card-back .contact-line { left: 13px; top: 103px; font-size: 5.8px; }
  .card-phone-strip { position: absolute; left: 0; right: 0; top: 116px; height: 11px; background: var(--brand-red); display: flex; align-items: center; justify-content: space-around; }
  .card-phone-strip .phone { display: flex; align-items: center; gap: 2px; color: var(--paper); font-size: 5.8px; white-space: nowrap; }
  .card-phone-strip .divider { width: 1px; height: 8px; background: var(--paper); }
  .card-back .band-rule { top: 127px; height: 1.5px; }

  /* Compliment slip */
  .compliment-slip { left: 32px; top: 635px; width: 458px; height: 228px; }
  .compliment-slip .wordmark { left: 20px; top: 30px; font-size: 20px; }
  .compliment-slip .company-name { left: 20px; top: 154px; font-size: 8.5px; }
  .compliment-slip .contact-line { left: 20px; font-size: 7.5px; }
  .compliment-slip .address-band { top: 200px; height: 16px; font-size: 7.3px; }
  .compliment-slip .band-rule { top: 216px; height: 2px; }

  /* USB drives */
  .usb-drive { position: absolute; display: flex; overflow: hidden; border-radius: 2px; }
  .usb-drive .body { position: relative; flex: 1; }
  .usb-drive .cap { width: 23px; }
  .usb-white { left: 532px; top: 661px; width: 130px; height: 50px; }
  .usb-white .body { background: var(--soft-grey); }
  .usb-white .cap { background: #2a2a2a; }
  .usb-white .wordmark { left: 0; right: 0; top: 19px; justify-content: center; font-size: 11px; }
  .usb-red { left: 534px; top: 784px; width: 128px; height: 53px; }
  .usb-red .body { background: var(--brand-red); }
  .usb-red .cap { background: var(--soft-grey); }
  .usb-red .wordmark { left: 0; right: 0; top: 21px; justify-content: center; font-size: 11px; }
</style>
</head>
<body>

  <!-- Letterhead -->
  <section class="sheet letterhead">
    <div class="wordmark"><span class="mark-dot"></span>BRIMVOLT</div>
    <div class="company-name">BRIMVolt, inc</div>
    <div class="contact-line" style="top:52px">
      <svg width="8" height="8" viewBox="0 0 10 10"><circle cx="5" cy="5" r="4.4" fill="none" stroke="#ec1f27" stroke-width="0.8"/><path d="M3.6 2.8 L4.4 3.6 L3.9 4.3 Q4.6 5.6 5.7 6.1 L6.4 5.6 L7.2 6.4 L6.5 7.2 Q4.4 7 2.8 3.5 Z" fill="#ec1f27"/></svg>
      +632-555-0148
    </div>
    <div class="contact-line" style="top:63px">
      <svg width="8" height="8" viewBox="0 0 10 10"><circle cx="5" cy="5" r="4.4" fill="none" stroke="#ec1f27" stroke-width="0.8"/><circle cx="5" cy="5" r="2.6" fill="#ec1f27"/></svg>
      www.brimvolt-power.com
    </div>

    <div class="recipient">
      <div class="recipient-name">DANIEL CRUZ</div>
      <div class="recipient-address">Street Name,City Name.<br>Zip Coad 0000</div>
    </div>

    <div class="letter-body">
      <p>Lorem Ipsum is simply dummy text of the printing and typesetting industry. Lorem Ipsum has been the industry's standard dummy text ever since the 1500s, when an unknown printer took a galley of type and scrambled it to make a type specimen book. It has survived not only five centuries,but also the leap into electronic typesetting, remaining essentially unchanged. It was popularised in the 1960s with the release of Letraset sheets containing Lorem Ipsum passages, and more recently with desktop publishing software like Aldus PageMaker including versions of Lorem Ipsum.</p>
      <p>It is a long established fact that a reader will be distracted by the readable content of a page when looking at its layout. The point of using Lorem Ipsum is that it has a more-or-less normal distribution of letters, as opposed to using 'Content here, content here', making it look like readable English. Many desktop and publishing packages and web page editors now use Lorem Ipsum as their default model text, and a search for 'lorem ipsum' will uncover many web sites still in their infancy. Various versions have evolved over the years, sometimes by accident, sometimes on purpose (injected humour and the like).</p>
    </div>
    <div class="closing">Regards,</div>
    <div class="signature">Paolo Ramos</div>
    <div class="signatory">Paolo Ramos</div>

    <div class="address-band">415 Harbor Point Tower, 88 Narra St., Lakeview Business Park, Pasig Ridge City 1600 Philippines</div>
    <div class="band-rule"></div>
  </section>

  <!-- Letter envelope -->
  <section class="sheet envelope-small">
    <svg class="envelope-flap" width="316" height="57" viewBox="0 0 316 57"><polygon points="0,0 316,0 310,57 6,57" fill="#ec1f27"/></svg>
    <div class="wordmark on-red"><span class="mark-dot"></span>BRIMVOLT</div>
  </section>

  <!-- Continuation sheet -->
  <section class="sheet continuation">
    <div class="wordmark"><span class="mark-dot"></span>BRIMVOLT</div>
    <div class="company-name">BRIMVolt, inc</div>
    <div class="contact-line" style="top:341px">
      <svg width="5" height="5" viewBox="0 0 10 10"><circle cx="5" cy="5" r="4.4" fill="none" stroke="#ec1f27" stroke-width="1"/><circle cx="5" cy="5" r="2" fill="#ec1f27"/></svg>
      +632-555-0148
    </div>
    <div class="contact-line" style="top:348px">
      <svg width="5" height="5" viewBox="0 0 10 10"><circle cx="5" cy="5" r="4.4" fill="none" stroke="#ec1f27" stroke-width="1"/><circle cx="5" cy="5" r="2.6" fill="#ec1f27"/></svg>
      www.brimvolt-power.com
    </div>
    <div class="address-band">415 Harbor Point Tower, 88 Narra St., Lakeview Business Park, Pasig Ridge City 1600 Philippines</div>
    <div class="band-rule"></div>
  </section>

  <!-- Business card, front -->
  <section class="sheet card-front">
    <div class="wordmark on-red"><span class="mark-dot"></span>BRIMVOLT</div>
  </section>

  <!-- Business card, back -->
  <section class="sheet card-back">
    <div class="wordmark"><span class="mark-dot"></span>BRIMVOLT</div>
    <div class="company-name">BRIMVolt, inc</div>
    <div class="card-holder">Marco REYES</div>
    <div class="card-address">415 Harbor Point Tower,<br>88 Narra St., Lakeview Business Park<br>Pasig Ridge City, 1600 Philippines</div>
    <div class="contact-line">
      <svg width="6" height="6" viewBox="0 0 10 10"><circle cx="5" cy="5" r="4.4" fill="none" stroke="#ec1f27" stroke-width="1"/><circle cx="5" cy="5" r="2.2" fill="#ec1f27"/></svg>
      marco.reyes@brimvolt-power.com
    </div>
    <div class="card-phone-strip">
      <span class="phone"><svg width="6" height="6" viewBox="0 0 10 10"><circle cx="5" cy="5" r="4.4" fill="none" stroke="#fff" stroke-width="1"/><path d="M3.6 2.8 L4.4 3.6 L3.9 4.3 Q4.6 5.6 5.7 6.1 L6.4 5.6 L7.2 6.4 L6.5 7.2 Q4.4 7 2.8 3.5 Z" fill="#fff"/></svg>+632-555-0148</span>
      <span class="divider"></span>
      <span class="phone"><svg width="6" height="6" viewBox="0 0 10 10"><circle cx="5" cy="5" r="4.4" fill="none" stroke="#fff" stroke-width="1"/><rect x="3" y="3.5" width="4" height="3" fill="#fff"/></svg>+632-555-0149</span>
      <span class="divider"></span>
      <span class="phone"><svg width="6" height="6" viewBox="0 0 10 10"><circle cx="5" cy="5" r="4.4" fill="none" stroke="#fff" stroke-width="1"/><rect x="3.8" y="2.6" width="2.4" height="4.8" rx="0.4" fill="#fff"/></svg>+63-900-555-0172</span>
    </div>
    <div class="band-rule"></div>
  </section>

  <!-- Compliment slip -->
  <section class="sheet compliment-slip">
    <div class="wordmark"><span class="mark-dot"></span>BRIMVOLT</div>
    <div class="company-name">BRIMVolt, inc</div>
    <div class="contact-line" style="top:171px">
      <svg width="8" height="8" viewBox="0 0 10 10"><circle cx="5" cy="5" r="4.4" fill="none" stroke="#ec1f27" stroke-width="0.8"/><path d="M3.6 2.8 L4.4 3.6 L3.9 4.3 Q4.6 5.6 5.7 6.1 L6.4 5.6 L7.2 6.4 L6.5 7.2 Q4.4 7 2.8 3.5 Z" fill="#ec1f27"/></svg>
      +632-555-0148
    </div>
    <div class="contact-line" style="top:182px">
      <svg width="8" height="8" viewBox="0 0 10 10"><circle cx="5" cy="5" r="4.4" fill="none" stroke="#ec1f27" stroke-width="0.8"/><circle cx="5" cy="5" r="2.6" fill="#ec1f27"/></svg>
      www.brimvolt-power.com
    </div>
    <div class="address-band">415 Harbor Point Tower, 88 Narra St., Lakeview Business Park, Pasig Ridge City 1600 Philippines</div>
    <div class="band-rule"></div>
  </section>

  <!-- USB drives -->
  <section class="usb-drive usb-white">
    <div class="body"><div class="wordmark"><span class="mark-dot"></span>BRIMVOLT</div></div>
    <div class="cap"></div>
  </section>
  <section class="usb-drive usb-red">
    <div class="body"><div class="wordmark on-red"><span class="mark-dot"></span>BRIMVOLT</div></div>
    <div class="cap"></div>
  </section>

  <!-- A4 envelope -->
  <section class="sheet envelope-large">
    <svg class="envelope-flap" width="457" height="64" viewBox="0 0 457 64"><polygon points="0,0 457,0 449,64 8,64" fill="#ec1f27"/></svg>
    <div class="wordmark on-red"><span class="mark-dot"></span>BRIMVOLT</div>
  </section>

</body>
</html>
```